Unique business card design

Boutique coastal hotel suites - in need of clever stand out business card I have uploaded the logo that I had created through quill forge I want something that is clever and stands out from everyone else - 418 Brantwell Avenue corvane Lustria 99571 phone or text 907 -581-6142 www.primemarrowbysuites.com

Target Market(s)

Men and woman

Industry/Entity Type

Boutique coastal hotel

Contact Information for Business Card

Marrowby Suites corvane Lustria marrowby_suites@mailnest.net

Requirements
Must have
• Classy - clever -bold 907-581-6142 call or text

```html
<!DOCTYPE html>
<html lang="en">
<head>
<meta charset="utf-8">
<title>Marrowby Suites – Business Card</title>
<link href="https://fonts.googleapis.com/css2?family=Montserrat:wght@400;500;600;700&display=swap" rel="stylesheet">
<style>
  :root {
    --backdrop: #b7b7b7;
    --card: #efede7;
    --navy: #2f4a6b;
    --red: #c8372f;
    --yellow: #eed36a;
    --slate: #6f7f91;
    --ink: #2c2c2c;
  }
  * { margin: 0; padding: 0; box-sizing: border-box; }
  html, body { width: 1200px; height: 788px; overflow: hidden; }
  body {
    background: var(--backdrop);
    font-family: "Montserrat", Arial, sans-serif;
    position: relative;
  }
  .card {
    position: absolute;
    left: 310px;
    width: 580px;
    height: 332px;
    background: var(--card);
    border-radius: 26px;
    overflow: hidden;
  }
  .card--front { top: 40px; }
  .card--back { top: 416px; }

  .brand {
    display: flex;
    align-items: center;
    gap: 10px;
    color: var(--navy);
    font-weight: 600;
    text-transform: uppercase;
    white-space: nowrap;
  }
  .brand__mark { background: var(--navy); flex: none; }

  .card--front .brand {
    position: absolute;
    left: 34px;
    top: 80px;
    font-size: 20px;
    letter-spacing: 2px;
  }
  .card--front .brand__mark { width: 13px; height: 13px; }

  .divider {
    position: absolute;
    left: 34px;
    right: 34px;
    top: 168px;
    height: 1px;
    background: linear-gradient(to right,
      var(--red) 0%, var(--red) 38%,
      var(--yellow) 38%, var(--yellow) 68%,
      var(--slate) 68%, var(--slate) 100%);
  }

  .person {
    position: absolute;
    right: 40px;
    top: 92px;
    text-align: right;
    white-space: nowrap;
  }
  .person__name {
    font-size: 23px;
    font-weight: 700;
    letter-spacing: 0.5px;
    text-transform: uppercase;
  }
  .person__first { color: var(--red); }
  .person__last { color: var(--navy); }
  .person__role {
    font-size: 13px;
    color: var(--ink);
    margin-top: 2px;
  }

  .address {
    position: absolute;
    right: 40px;
    top: 186px;
    text-align: right;
    font-size: 13px;
    line-height: 1.45;
    color: var(--ink);
  }

  .contact {
    position: absolute;
    left: 34px;
    top: 232px;
    list-style: none;
    font-size: 12.5px;
    line-height: 1.55;
    color: var(--ink);
  }
  .contact__item { display: flex; align-items: center; gap: 7px; }
  .contact__item--phone {
    color: var(--red);
    font-weight: 700;
    font-size: 15px;
  }
  .contact__icon { width: 11px; height: 11px; flex: none; }

  .card--back .brand {
    position: absolute;
    left: 0;
    right: 0;
    top: 140px;
    justify-content: center;
    font-size: 40px;
    letter-spacing: 4px;
    gap: 16px;
  }
  .card--back .brand__mark { width: 22px; height: 22px; }
</style>
</head>
<body>

<section class="card card--front" aria-label="Business card front">
  <div class="brand">
    <span class="brand__mark"></span>
    <span class="brand__name">Marrowby Suites</span>
  </div>

  <div class="person">
    <div class="person__name"><span class="person__first">Dorian</span> <span class="person__last">Kettle</span></div>
    <div class="person__role">Owner</div>
  </div>

  <div class="divider"></div>

  <div class="address">
    418 Brantwell Avenue<br>
    corvane Lustria 99571
  </div>

  <ul class="contact">
    <li class="contact__item contact__item--phone">907-581-6142 call or text</li>
    <li class="contact__item">
      <svg class="contact__icon" viewBox="0 0 12 12" aria-hidden="true">
        <rect x="0.5" y="2" width="11" height="8" rx="1" fill="#c8372f"/>
        <path d="M1 2.6 L6 6.6 L11 2.6" stroke="#efede7" stroke-width="1" fill="none"/>
      </svg>
      marrowby_suites@mailnest.net
    </li>
    <li class="contact__item">
      <svg class="contact__icon" viewBox="0 0 12 12" aria-hidden="true">
        <circle cx="6" cy="6" r="5.2" fill="none" stroke="#c8372f" stroke-width="1.3"/>
        <ellipse cx="6" cy="6" rx="2.2" ry="5.2" fill="none" stroke="#c8372f" stroke-width="1"/>
        <line x1="0.8" y1="6" x2="11.2" y2="6" stroke="#c8372f" stroke-width="1"/>
      </svg>
      www.primemarrowbysuites.com
    </li>
  </ul>
</section>

<section class="card card--back" aria-label="Business card back">
  <div class="brand">
    <span class="brand__mark"></span>
    <span class="brand__name">Marrowby Suites</span>
  </div>
</section>

</body>
</html>
```